Stationary and business card design for ministry
Global Neighbor Fellowship
Stationary and business card design for ministry - Religion and Spirituality
Creative Brief
Bright & Fun-filled
Dwight R. Pembrook III
Executive Director
PO Box 582916 Tulsa, OK 74150
dwight@gnfhaven.org
www.gnfhaven.org
I have a few different ideas about the back of the business card. It could have the logo on the back with this tag line below it: "Reaching the world at our doorstep." However, this tag line could also be on the front, and just the logo on the back with the web address below. Another option is to have just GNF (see uploads) on the front, and the full logo on the back or the other way around.
See instructions under the additional comments.

```html
<!DOCTYPE html>
<html lang="en">
<head>
<meta charset="utf-8">
<title>Global Neighbor Fellowship — Stationery Set</title>
<link rel="stylesheet" href="https://fonts.googleapis.com/css2?family=Montserrat:wght@400;600;700&display=swap">
<style>
  :root {
    --green: #7cb342;
    --green-dark: #5e9a2a;
    --green-light: #a5cf74;
    --ink: #1e1e1e;
    --grey: #9a9a9a;
    --paper: #ffffff;
    --backdrop: #5b5d60;
    --globe-paper: #e4e4e4;
  }
  * { box-sizing: border-box; margin: 0; padding: 0; }
  html, body { width: 1200px; height: 961px; overflow: hidden; }
  body {
    background: var(--backdrop);
    font-family: "Montserrat", Arial, sans-serif;
    position: relative;
  }
  .piece { position: absolute; overflow: hidden; box-shadow: 0 6px 18px rgba(0,0,0,.35); }

  /* brand lockup */
  .brand { display: flex; align-items: center; gap: 8px; }
  .brand-dot { width: 14px; height: 14px; border-radius: 50%; background: currentColor; flex: none; }
  .brand-text { font-weight: 700; line-height: 1.05; }
  .brand-text .brand-initials { display: block; font-size: 34px; letter-spacing: 1px; }
  .brand-text .brand-name { display: block; font-size: 10px; max-width: 120px; }
  .brand--light { color: var(--paper); }
  .brand--green { color: var(--green); }

  .globe { position: absolute; border-radius: 50%; }

  /* folder */
  .folder { left: 60px; top: 60px; width: 340px; height: 460px; background: var(--green); }
  .folder .brand { position: absolute; top: 34px; right: 28px; }
  .folder .globe {
    left: -40px; top: 150px; width: 320px; height: 320px;
    background: radial-gradient(circle at 40% 40%, var(--green-light), var(--green) 75%);
    opacity: .75;
  }

  /* letterhead */
  .letterhead { left: 430px; top: 60px; width: 340px; height: 460px; background: var(--paper); }
  .letterhead .brand { position: absolute; top: 28px; left: 28px; }
  .letterhead .globe {
    left: 20px; top: 140px; width: 230px; height: 230px;
    background: radial-gradient(circle at 40% 40%, #f2f2f2, var(--globe-paper) 75%);
  }

  .swoosh { position: absolute; left: 0; bottom: 0; width: 100%; display: block; }

  /* disc */
  .disc {
    left: 810px; top: 80px; width: 330px; height: 330px; border-radius: 50%;
    background: var(--green);
  }
  .disc .brand { position: absolute; top: 58px; left: 50%; transform: translateX(-50%); }
  .disc-hub {
    position: absolute; left: 50%; top: 50%; width: 96px; height: 96px; margin: -48px 0 0 -48px;
    border-radius: 50%; background: #c9c9c9; border: 14px solid #8e8e8e;
  }
  .disc-hole {
    position: absolute; left: 50%; top: 50%; width: 30px; height: 30px; margin: -15px 0 0 -15px;
    border-radius: 50%; background: var(--backdrop);
  }

  /* envelope */
  .envelope { left: 60px; top: 570px; width: 480px; height: 250px; background: var(--paper); }
  .envelope .brand { position: absolute; top: 24px; left: 24px; }
  .envelope .globe {
    right: 40px; top: 20px; width: 170px; height: 170px;
    background: radial-gradient(circle at 40% 40%, #f4f4f4, var(--globe-paper) 75%);
  }

  /* business cards */
  .card { width: 290px; height: 170px; }
  .card-front { left: 580px; top: 570px; background: var(--paper); }
  .card-back { left: 890px; top: 570px; background: var(--green); display: flex; align-items: center; justify-content: center; }
  .card-front .brand { position: absolute; top: 18px; left: 18px; }
  .card-front .brand-initials { font-size: 26px; }
  .card-front .brand-name { font-size: 8px; max-width: 96px; }
  .contact { position: absolute; top: 18px; right: 16px; text-align: right; font-size: 7.5px; line-height: 1.55; color: var(--ink); }
  .contact .contact-name { font-weight: 700; font-size: 9px; color: var(--green-dark); }
  .contact .contact-title { font-weight: 600; margin-bottom: 4px; }
  .card-back .tagline { position: absolute; bottom: 18px; width: 100%; text-align: center; color: var(--paper); font-size: 9px; font-weight: 600; }
</style>
</head>
<body>

  <section class="piece folder" aria-label="Presentation folder">
    <div class="globe" role="img" aria-label="Faint world globe illustration"></div>
    <div class="brand brand--light">
      <span class="brand-dot"></span>
      <span class="brand-text"><span class="brand-initials">GNF</span><span class="brand-name">Global Neighbor Fellowship</span></span>
    </div>
  </section>

  <section class="piece letterhead" aria-label="Letterhead">
    <div class="brand brand--green">
      <span class="brand-dot"></span>
      <span class="brand-text"><span class="brand-initials">GNF</span><span class="brand-name">Global Neighbor Fellowship</span></span>
    </div>
    <div class="globe" role="img" aria-label="Faint world globe illustration"></div>
    <svg class="swoosh" viewBox="0 0 340 80" preserveAspectRatio="none" height="80">
      <path d="M0 80 L0 58 C110 34 230 26 340 8 L340 80 Z" fill="var(--green)"/>
      <path d="M0 50 C110 26 230 16 340 2" fill="none" stroke="var(--ink)" stroke-width="5"/>
      <path d="M0 40 C110 18 230 8 340 -4" fill="none" stroke="var(--grey)" stroke-width="3"/>
    </svg>
  </section>

  <section class="piece disc" aria-label="Disc label">
    <div class="brand brand--light">
      <span class="brand-dot"></span>
      <span class="brand-text"><span class="brand-initials">GNF</span></span>
    </div>
    <div class="disc-hub"></div>
    <div class="disc-hole"></div>
  </section>

  <section class="piece envelope" aria-label="Envelope">
    <div class="brand brand--green">
      <span class="brand-dot"></span>
      <span class="brand-text"><span class="brand-initials">GNF</span><span class="brand-name">Global Neighbor Fellowship</span></span>
    </div>
    <div class="globe" role="img" aria-label="Faint world globe illustration"></div>
    <svg class="swoosh" viewBox="0 0 480 70" preserveAspectRatio="none" height="70">
      <path d="M0 70 L0 56 C160 38 320 28 480 8 L480 70 Z" fill="var(--green)"/>
      <path d="M0 48 C160 30 320 18 480 0" fill="none" stroke="var(--ink)" stroke-width="5"/>
      <path d="M0 38 C160 22 320 10 480 -6" fill="none" stroke="var(--grey)" stroke-width="3"/>
    </svg>
  </section>

  <section class="piece card card-front" aria-label="Business card front">
    <div class="brand brand--green">
      <span class="brand-dot"></span>
      <span class="brand-text"><span class="brand-initials">GNF</span><span class="brand-name">Global Neighbor Fellowship</span></span>
    </div>
    <div class="contact">
      <p class="contact-name">Dwight R. Pembrook III</p>
      <p class="contact-title">Executive Director</p>
      <p>PO Box 582916 Tulsa, OK 74150</p>
      <p>dwight@gnfhaven.org</p>
      <p>www.gnfhaven.org</p>
    </div>
    <svg class="swoosh" viewBox="0 0 290 50" preserveAspectRatio="none" height="50">
      <path d="M0 50 L0 38 C100 26 200 18 290 6 L290 50 Z" fill="var(--green)"/>
      <path d="M0 32 C100 20 200 12 290 0" fill="none" stroke="var(--ink)" stroke-width="4"/>
      <path d="M0 25 C100 14 200 6 290 -5" fill="none" stroke="var(--grey)" stroke-width="2"/>
    </svg>
  </section>

  <section class="piece card card-back" aria-label="Business card back">
    <div class="brand brand--light">
      <span class="brand-dot"></span>
      <span class="brand-text"><span class="brand-initials">GNF</span><span class="brand-name">Global Neighbor Fellowship</span></span>
    </div>
    <p class="tagline">Reaching the world at our doorstep.</p>
  </section>

</body>
</html>
```